Customer Loyalty Card - Tourism - Tour Card

We would like to make a loyalty card for our tour business. If someone books 1 full priced tour they then get 10% off the 2nd tour and 10% off the 3rd tour and 15% off the 4th tour they do with us. All bookings must be booked directly with Kestrel Bay Wildlife Tours

View our website for design and colour ideas www.kestrelbaywildlifetours.com

Target Market(s)

People on holidays doing tours on Lord Howe Island

Industry/Entity Type

Travel

Contact Information for Business Card

www.kestrelbaywildlifetours.com
Im looking for a 1 sided card - if possible.

Phone, email and address are probably not really required. I will need to stamp the card once a tour has been booked and paid for. There is no name and position, its just a business card sized Loyalty Card.

Requirements
Must have
• Logo
• I will need to stamp the card once a tour has been booked and paid for.

```html
<!DOCTYPE html>
<html lang="en">
<head>
<meta charset="utf-8">
<title>Kestrel Bay Wildlife Tours – Loyalty Card</title>
<link href="https://fonts.googleapis.com/css2?family=Lilita+One&family=Josefin+Sans:wght@300&family=Caveat+Brush&display=swap" rel="stylesheet">
<style>
  :root {
    --sky: #cfe3ee;
    --mountain: #46584f;
    --forest: #2f4a2c;
    --forest-light: #4d6b3a;
    --lagoon: #2fb3c4;
    --lagoon-deep: #1f7fa6;
    --sand: #e9e4d2;
    --ink: #0b0b0b;
    --paper: #ffffff;
    --stamp-text: #bcbcbc;
    --script: rgba(236, 236, 236, 0.9);
  }
  * { margin: 0; padding: 0; box-sizing: border-box; }
  html, body { width: 1200px; height: 686px; overflow: hidden; background: #f2f2f2; }

  .loyalty-card {
    position: relative;
    width: 1200px;
    height: 686px;
    overflow: hidden;
    font-family: "Lilita One", sans-serif;
  }

  .island-photo {
    position: absolute;
    inset: 0;
    background:
      radial-gradient(ellipse 520px 260px at 820px 60px, #5b6a62 0%, rgba(91,106,98,0) 70%),
      radial-gradient(ellipse 420px 160px at 280px 660px, var(--lagoon) 0%, rgba(47,179,196,0) 75%),
      radial-gradient(ellipse 260px 60px at 560px 520px, var(--sand) 0%, rgba(233,228,210,0) 80%),
      linear-gradient(180deg,
        var(--sky) 0%,
        #b4cfdb 12%,
        var(--mountain) 20%,
        var(--lagoon-deep) 30%,
        var(--forest-light) 38%,
        var(--forest) 55%,
        #35502f 70%,
        var(--lagoon) 86%,
        var(--lagoon-deep) 100%);
  }

  .brand-mark {
    position: absolute;
    left: 19px;
    top: 47px;
    width: 376px;
    height: 376px;
    border-radius: 50%;
    background: var(--ink);
    display: flex;
    align-items: center;
    justify-content: center;
    text-align: center;
    color: var(--paper);
    font-size: 44px;
    line-height: 1.1;
    padding: 40px;
    letter-spacing: 1px;
  }

  .title-banner {
    position: absolute;
    left: 377px;
    top: 123px;
    width: 737px;
    height: 126px;
    background: var(--ink);
    border-radius: 0 24px 24px 0;
    display: flex;
    align-items: center;
    justify-content: flex-end;
    padding-right: 40px;
  }
  .title-banner h1 {
    color: var(--paper);
    font-size: 92px;
    font-weight: 400;
    letter-spacing: 3px;
    line-height: 1;
  }

  .tagline {
    position: absolute;
    left: 500px;
    top: 262px;
    width: 560px;
    text-align: center;
  }
  .tagline-lead {
    display: block;
    font-family: "Josefin Sans", sans-serif;
    font-weight: 300;
    font-size: 36px;
    letter-spacing: 6px;
    color: var(--script);
  }
  .tagline-script {
    display: block;
    font-family: "Caveat Brush", cursive;
    font-size: 170px;
    line-height: 0.9;
    color: var(--script);
    margin-top: -6px;
  }

  .stamp-row {
    position: absolute;
    left: 78px;
    top: 491px;
    display: flex;
    gap: 27px;
  }
  .stamp-slot {
    width: 240px;
    height: 111px;
    background: var(--paper);
    border: 8px solid var(--ink);
    border-radius: 20px;
    display: flex;
    flex-direction: column;
    align-items: center;
    justify-content: center;
    color: var(--stamp-text);
    font-size: 44px;
    line-height: 0.95;
    letter-spacing: 1px;
    text-align: center;
  }
  .stamp-slot sup { font-size: 24px; vertical-align: 16px; line-height: 0; }
</style>
</head>
<body>
  <main class="loyalty-card">
    <div class="island-photo" role="img" aria-label="Aerial photograph of a green forested island with twin mountains, white beaches and a turquoise lagoon"></div>

    <div class="brand-mark">Kestrel Bay Wildlife Tours</div>

    <div class="title-banner"><h1>LOYALTY CARD</h1></div>

    <p class="tagline">
      <span class="tagline-lead">PLAN YOUR NEXT</span>
      <span class="tagline-script">Adventure</span>
    </p>

    <section class="stamp-row" aria-label="Tour stamps">
      <div class="stamp-slot"><span>FIRST</span><span>TOUR</span></div>
      <div class="stamp-slot"><span>2<sup>ND</sup> TOUR</span><span>10% OFF</span></div>
      <div class="stamp-slot"><span>3<sup>RD</sup> TOUR</span><span>10% OFF</span></div>
      <div class="stamp-slot"><span>4<sup>TH</sup> TOUR</span><span>15% OFF</span></div>
    </section>
  </main>
</body>
</html>
```